law firm website

We need a website for our law firm that is based in Kabul, Afghanistan. We provide legal and government affairs services for the international community. We would like to see designs that use the colors of our logo, designs that are elegant and simple, yet not boring or over the top. No law or law related symbols or pictures. We would like clocks that show times for Kabul, Dubai and Washington DC.
Updates
Reason: No designs that are up to the task as yet. Perhaps we should stop using picture of people, that obviously don't work with us, in the website. If you are to use pictures, please try using pictures of Afghanistan mountains, art, craft etc. Also, please make the clocks very small - they seem to be dominating the website. We do not sell clocks or watches - we are a law firm. Hope you all understand and thank you for your designs to date.
Deal All,
Industry/Entity Type
Government
Requirements
Must have
- our logo.
the following phrases/words in flash.
"international standards" "local expertise" "integrity" "clarity" "commitment" "Afghanistan"
clocks: kabul, dubai, washington dc
Should not have
- law related pictures
afghanistan flag colors

```html
<!DOCTYPE html>
<html lang="en">
<head>
<meta charset="utf-8">
<title>Hindukush Counsel Group</title>
<link rel="stylesheet" href="https://fonts.googleapis.com/css2?family=Arimo:wght@400;700&display=swap">
<style>
:root{
  --brand-blue:#0a86cc;
  --brand-blue-light:#12b2e6;
  --brand-blue-dark:#0a6fb8;
  --heading-blue:#7f9fbd;
  --logo-grey:#7d8c9e;
  --text-grey:#8a8a8a;
  --text-dark:#222;
  --link-blue:#1a6fc0;
  --rule:#d8d8d8;
  --icon-grey:#8f9297;
}
*{margin:0;padding:0;box-sizing:border-box}
html,body{width:1125px;height:1200px;overflow:hidden;background:#fff}
body{position:relative;font-family:"Arimo",Arial,sans-serif;color:var(--text-grey)}
.abs{position:absolute}

.brand{left:136px;top:22px;display:flex;align-items:center;gap:10px}
.brand-mark{width:34px;height:34px;background:var(--logo-grey)}
.brand-name{font-size:15px;line-height:18px;color:var(--logo-grey);letter-spacing:.6px;text-transform:uppercase;width:160px}

.search{left:820px;top:40px;width:171px;height:28px;border:1px solid #c6c6c6;border-radius:3px;font-size:12px;color:#555;padding:7px 8px}
.search svg{position:absolute;right:8px;top:7px}

.main-nav{left:132px;top:83px;width:861px;height:43px;background:linear-gradient(var(--brand-blue-light),var(--brand-blue-dark));display:flex;align-items:center}
.main-nav a{color:#fff;text-decoration:none;font-size:14.5px;position:absolute;top:13px}

.hero{left:132px;top:126px;width:861px;height:353px;background:linear-gradient(180deg,#b9c6ea 0%,#8ea6d8 35%,#5c6d9e 60%,#aab7dc 75%,#6d7fb5 100%)}
.hero-word{color:#fff;font-size:21px;top:60px;position:absolute}
.hero-arrow{position:absolute;top:163px}

.welcome{left:132px;top:496px;width:861px;text-align:center}
.welcome h1{font-weight:400;font-size:19px;color:var(--text-dark);margin-bottom:12px}
.welcome p{font-size:11.5px;line-height:19.4px}

.section-title{font-weight:400;font-size:15px;color:var(--heading-blue)}

.about-photo{left:132px;top:662px;width:286px;height:192px;background:linear-gradient(120deg,#f3ecdf 0%,#d9b79a 45%,#5a6470 100%);border:1px solid #ddd}
.about-text{left:456px;top:660px;width:535px;font-size:11.5px;line-height:22px}
.btn{left:456px;top:825px;width:91px;height:29px;border-radius:3px;background:linear-gradient(var(--brand-blue-light),var(--brand-blue-dark));color:#fff;font-size:11.5px;text-align:center;line-height:29px}

.col-text{font-size:11.5px;line-height:22px}
.divider{width:1px;background:#888;top:925px;height:144px}

.clock-label{font-size:12px;color:var(--text-grey);top:946px;position:absolute}

.footer-rule{left:0;top:1106px;width:1125px;height:1px;background:var(--rule)}
.footer-nav{left:134px;top:1128px;font-size:11.5px;color:#444;word-spacing:2px}
.footer-nav span{margin:0 9px}
.copyright{left:134px;top:1155px;font-size:11.5px;color:#444}
.follow{left:639px;top:1146px;font-size:11.5px;color:#444}
.social{top:1142px;width:21px;height:21px;border-radius:50%;background:var(--icon-grey)}
.partner{left:918px;top:1120px;width:40px;height:40px;border-radius:50%;background:linear-gradient(#c9d3dc,#7e96ad)}
</style>
</head>
<body>

<header>
  <div class="abs brand"><div class="brand-mark"></div><div class="brand-name">Hindukush Counsel Group</div></div>
  <div class="abs search">Search
    <svg width="14" height="14" viewBox="0 0 14 14"><circle cx="5.5" cy="5.5" r="4" fill="none" stroke="#888" stroke-width="1.5"/><line x1="8.5" y1="8.5" x2="13" y2="13" stroke="#888" stroke-width="2"/></svg>
  </div>
  <nav class="abs main-nav">
    <a style="left:63px">Home</a>
    <a style="left:182px">About us</a>
    <a style="left:320px">Services</a>
    <a style="left:456px">Testimonials</a>
    <a style="left:618px">Blog</a>
    <a style="left:727px">Contact us</a>
  </nav>
</header>

<section class="abs hero" role="img" aria-label="Snow-covered mountain peak reflected in a calm lake">
  <span class="hero-word" style="left:456px">Integrity</span>
  <span class="hero-word" style="left:582px">Clarity</span>
  <span class="hero-word" style="left:692px">Commitment</span>
  <svg class="hero-arrow" style="left:20px" width="32" height="32" viewBox="0 0 32 32"><circle cx="16" cy="16" r="14.5" fill="rgba(255,255,255,.15)" stroke="rgba(255,255,255,.5)" stroke-width="1.5"/><path d="M19 9l-7 7 7 7" fill="none" stroke="rgba(255,255,255,.6)" stroke-width="2"/></svg>
  <svg class="hero-arrow" style="left:800px" width="32" height="32" viewBox="0 0 32 32"><circle cx="16" cy="16" r="14.5" fill="rgba(255,255,255,.15)" stroke="rgba(255,255,255,.5)" stroke-width="1.5"/><path d="M13 9l7 7-7 7" fill="none" stroke="rgba(255,255,255,.6)" stroke-width="2"/></svg>
</section>

<section class="abs welcome">
  <h1>Welcome To HCG</h1>
  <p>Managing Partner of a specialist dispute resolution law firm in Kabul, Afghanistan. Prof. Danesh is Chancellor of, and Professor of Law at, Pamir University, Kabul, Afghanistan.&nbsp; In addition to lecturing at Pamir University, Professor Danesh is frequently called upon to train high-ranking Government of Afghanistan officials on legal and diplomatic matters.&nbsp; He is a regular speaker at conferences on issues relating to rule of law and economic development and often features on television programs where topical legal issues are discussed.</p>
</section>

<h2 class="abs section-title" style="left:133px;top:623px">About us</h2>
<div class="abs about-photo" role="img" aria-label="Portrait photo of firm staff"></div>
<p class="abs about-text">Managing Partner of a specialist dispute resolution law firm in Kabul, Afghanistan. Prof. Danesh is Chancellor of, and Professor of Law at, Pamir University, Kabul, Afghanistanlecturing at Pamir University-Managing Partner of a specialist dispute resolution law firm in Kabul, Afghanistan. Prof. Danesh is Chancellor of, and Professor of Law at, Pamir University, Kabul, Afghanistan.&nbsp; In addition to lecturing at Pamir University, Professor Danesh is frequently called upon to train high-ranking Government of Afghanistan officials on legal and diplomatic matterscalled upon to train high-ranking Government of Afghanistan officials on legal and diplomatic matters....</p>
<div class="abs btn">Read more</div>

<h2 class="abs section-title" style="left:134px;top:880px">Services</h2>
<svg class="abs" style="left:133px;top:920px" width="29" height="29" viewBox="0 0 29 29"><circle cx="14.5" cy="14.5" r="13.5" fill="#fff" stroke="#bbb"/><path d="M12 8.5l6 6-6 6" fill="none" stroke="#333" stroke-width="1.6"/></svg>
<p class="abs col-text" style="left:169px;top:924px;width:220px">Managing Partner of a specialist dispute resolution law firm in Kabul, Afghanistan. Prof. Danesh is Chancellor of, and Profes-sor of Law at, Pamir University, Kabul, Afghanistanlecturing at Pamir University-Managing Partner of a specialist dispute resolution law ...</p>
<div class="abs divider" style="left:432px"></div>

<h2 class="abs section-title" style="left:464px;top:880px">Testimonials</h2>
<svg class="abs" style="left:700px;top:902px" width="24" height="12" viewBox="0 0 24 12"><path d="M6 1l-5 5 5 5M18 1l5 5-5 5" fill="none" stroke="#999" stroke-width="1.2"/></svg>
<p class="abs col-text" style="left:469px;top:924px;width:232px">Managing Partner of a specialist dispute resolution law firm in Kabul, Afghanistan. Prof. Danesh is Chancellor of, and Professor of Law at, Pamir University, Kabul, Afghani-stanlecturing at Pamir ...</p>
<p class="abs" style="left:470px;top:1041px;font-size:11.5px;color:var(--link-blue)">Marcus</p>
<p class="abs" style="left:472px;top:1064px;font-size:9.5px;color:var(--link-blue)">Posed on 15 dec 2013</p>
<div class="abs divider" style="left:732px"></div>

<h2 class="abs section-title" style="left:768px;top:880px">Clocks</h2>
<span class="clock-label" style="left:770px">kabul</span>
<span class="clock-label" style="left:844px">dubai</span>
<span class="clock-label" style="left:905px">washington</span>
<svg class="abs" style="left:754px;top:968px" width="220" height="64" viewBox="0 0 220 64">
  <defs><radialGradient id="face" cx=".4" cy=".35" r=".7"><stop offset="0" stop-color="#fff"/><stop offset="1" stop-color="#d4dce2"/></radialGradient></defs>
  <g transform="translate(32,32)">
    <circle r="30" fill="#b9c0c6"/><circle r="26" fill="url(#face)"/>
    <line x1="0" y1="0" x2="17" y2="0" stroke="#333" stroke-width="1.8"/><line x1="0" y1="0" x2="0" y2="-21" stroke="#333" stroke-width="1.2"/>
  </g>
  <g transform="translate(109,32)">
    <circle r="30" fill="#b9c0c6"/><circle r="26" fill="url(#face)"/>
    <line x1="0" y1="0" x2="0" y2="17" stroke="#333" stroke-width="1.8"/><line x1="0" y1="0" x2="0" y2="-21" stroke="#333" stroke-width="1.2"/>
  </g>
  <g transform="translate(185,32)">
    <circle r="30" fill="#b9c0c6"/><circle r="26" fill="url(#face)"/>
    <line x1="0" y1="0" x2="-6" y2="-15" stroke="#333" stroke-width="1.8"/><line x1="0" y1="0" x2="5" y2="10" stroke="#333" stroke-width="1.2"/>
  </g>
</svg>

<footer>
  <div class="abs footer-rule"></div>
  <p class="abs footer-nav">Home<span>|</span>About us<span>|</span>Services<span>|</span>Testimonials<span>|</span>Blog<span>|</span>Contact us</p>
  <p class="abs copyright">Copyright 2013 HCG.All Right Reserved.</p>
  <p class="abs follow">Follow us &nbsp;:</p>
  <div class="abs social" style="left:716px"></div>
  <div class="abs social" style="left:745px"></div>
  <div class="abs social" style="left:773px"></div>
  <div class="abs partner"></div>
</footer>

</body>
</html>
```